Stationery Design Project

We need a stationary design (business card, logo, letterhead) for a new company called "Meridel Kestrova".
We provide software and consulting services to improve business efficiency & increase team engagement.
We focus on workflow automation, business social networking software and collaboration and communication tools built on mobile platforms.
Updates

Target Market(s)

Business with multi-site,young, mobile workforces e.g Retailers, Hospitality

Industry/Entity Type

Communication

Requirements
Must have
• Letterhead to include;
Business Address: 17 Wendle St, Corvath Vale, NSW 2100
ABN : 48 615 207 392

```html
<!DOCTYPE html>
<html lang="en">
<head>
<meta charset="utf-8">
<title>Meridel Kestrova Stationery</title>
<link rel="stylesheet" href="https://fonts.googleapis.com/css2?family=Open+Sans:wght@400;600;700&display=swap">
<style>
  :root {
    --teal: #22b0a3;
    --teal-light: #7fd6cc;
    --brown: #4e403a;
    --paper: #ffffff;
    --backdrop: #d4d4d4;
    --ink: #3d3330;
  }
  * { margin: 0; padding: 0; box-sizing: border-box; }
  html, body { width: 1200px; height: 900px; overflow: hidden; }
  body {
    background: var(--backdrop);
    font-family: "Open Sans", Verdana, sans-serif;
    color: var(--ink);
    position: relative;
  }
  .brand {
    display: flex;
    align-items: center;
    gap: 8px;
    color: var(--brown);
    font-weight: 700;
    line-height: 1;
  }
  .brand-dot {
    border-radius: 50%;
    background: var(--teal);
    flex: none;
  }

  /* Letterhead */
  .letterhead {
    position: absolute;
    left: 170px; top: 15px;
    width: 625px; height: 850px;
    background: var(--paper);
    box-shadow: 0 2px 10px rgba(0,0,0,.25);
    overflow: hidden;
  }
  .letterhead .brand { position: absolute; left: 38px; top: 50px; font-size: 27px; }
  .letterhead .brand-dot { width: 36px; height: 36px; }
  .letterhead-web {
    position: absolute; right: 70px; top: 28px;
    font-size: 10px; color: var(--teal);
  }
  .letterhead-address {
    position: absolute; left: 458px; top: 737px;
    font-size: 11px; line-height: 15px; color: var(--ink);
  }
  .contact-line { display: flex; align-items: center; gap: 5px; }
  .contact-icon { width: 9px; height: 9px; flex: none; }
  .letterhead-swoosh { position: absolute; left: 0; bottom: 0; width: 625px; height: 40px; }

  /* Business card front */
  .card {
    position: absolute;
    width: 262px; height: 145px;
    border-radius: 7px;
    overflow: hidden;
    box-shadow: 0 2px 6px rgba(0,0,0,.3);
  }
  .card-front { left: 708px; top: 232px; background: var(--paper); }
  .card-front .brand { position: absolute; left: 20px; top: 18px; font-size: 13px; gap: 5px; }
  .card-front .brand-dot { width: 18px; height: 18px; }
  .card-person { position: absolute; left: 18px; top: 62px; }
  .card-name { font-size: 10px; font-weight: 700; color: var(--brown); }
  .card-title { font-size: 7px; color: var(--teal); }
  .card-contacts {
    position: absolute; left: 14px; top: 103px;
    font-size: 6.5px; line-height: 9px; color: var(--ink);
  }
  .card-contacts .contact-icon { width: 6px; height: 6px; }
  .card-swoosh { position: absolute; left: 0; bottom: 0; width: 262px; height: 16px; }

  /* Business card back */
  .card-back {
    left: 698px; top: 398px; height: 155px;
    background: radial-gradient(ellipse at 55% 45%, var(--teal-light) 0%, var(--teal) 62%);
    color: #fff;
  }
  .card-back .brand { position: absolute; left: 40px; top: 40px; font-size: 19px; gap: 7px; }
  .card-back .brand-dot { width: 26px; height: 26px; background: #fff; }
  .card-services {
    position: absolute; left: 0; right: 0; top: 84px;
    text-align: center; font-size: 7.5px; line-height: 10px; list-style: none;
    padding-left: 50px;
  }
  .card-web {
    position: absolute; left: 0; right: 0; bottom: 20px;
    text-align: center; font-size: 7px; font-weight: 700;
  }
  .card-edge { position: absolute; left: 0; width: 262px; height: 14px; }
  .card-edge.top { top: 0; }
  .card-edge.bottom { bottom: 0; }
</style>
</head>
<body>

<section class="letterhead">
  <div class="brand"><span class="brand-dot"></span><span class="brand-name">Meridel Kestrova</span></div>
  <p class="letterhead-web">www.meridelkestrova.com</p>
  <address class="letterhead-address" style="font-style:normal">
    <div>17 Wendle St</div>
    <div>Corvath Vale NSW 2100</div>
    <div class="contact-line">
      <svg class="contact-icon" viewBox="0 0 10 10"><rect width="10" height="10" rx="2" fill="#22b0a3"/><path d="M3 2.5l1.2 1.3-.7.8a4 4 0 0 0 2 2l.8-.7L7.5 7 6.8 8A5 5 0 0 1 2 3.2z" fill="#fff"/></svg>
      <span>+61 2 7104 5620</span>
    </div>
    <div>ABN: 48 615 207 392</div>
  </address>
  <svg class="letterhead-swoosh" viewBox="0 0 625 40" preserveAspectRatio="none">
    <path d="M0 40 L0 28 Q300 -2 625 14 L625 40 Z" fill="#22b0a3"/>
    <path d="M0 40 L0 34 Q300 8 625 20 L625 40 Z" fill="#fff" opacity="0"/>
  </svg>
</section>

<section class="card card-front">
  <div class="brand"><span class="brand-dot"></span><span class="brand-name">Meridel Kestrova</span></div>
  <div class="card-person">
    <div class="card-name">Harlan Voss</div>
    <div class="card-title">Director</div>
  </div>
  <div class="card-contacts">
    <div class="contact-line"><svg class="contact-icon" viewBox="0 0 10 10"><rect width="10" height="10" rx="2" fill="#22b0a3"/></svg><span>+61 2 7104 5620</span></div>
    <div class="contact-line"><svg class="contact-icon" viewBox="0 0 10 10"><rect x="2" width="6" height="10" rx="1.5" fill="#22b0a3"/></svg><span>+61 452 390 184</span></div>
    <div class="contact-line"><svg class="contact-icon" viewBox="0 0 10 10"><rect y="2" width="10" height="6" fill="#22b0a3"/></svg><span>harlan.voss@meridelkestrova.com</span></div>
  </div>
  <svg class="card-swoosh" viewBox="0 0 262 16" preserveAspectRatio="none">
    <path d="M0 16 L0 4 Q130 12 262 8 L262 16 Z" fill="#22b0a3"/>
  </svg>
</section>

<section class="card card-back">
  <svg class="card-edge top" viewBox="0 0 262 14" preserveAspectRatio="none">
    <path d="M0 0 L262 0 L262 10 Q130 -2 0 8 Z" fill="#fff"/>
  </svg>
  <div class="brand"><span class="brand-dot"></span><span class="brand-name" style="color:var(--brown)">Meridel Kestrova</span></div>
  <ul class="card-services">
    <li>• Enterprise Social Networks</li>
    <li>• Workflow Automation</li>
    <li>• Training</li>
  </ul>
  <p class="card-web">www.meridelkestrova.com</p>
  <svg class="card-edge bottom" viewBox="0 0 262 14" preserveAspectRatio="none">
    <path d="M0 14 L0 4 Q130 14 262 4 L262 14 Z" fill="#fff"/>
  </svg>
</section>

</body>
</html>
```